Marvo Pour Over Coffee Filter Packaging Design

We are a brand new company starting to sell coffee related products. The coffee filter that we are about to sell will be copper color. We are working on the exact product picture, but a temporary one will be in uploaded files.We want the box to be simple, yet elegant and not too flashy. We prefer black, rose gold, white design, but are open to other designs. The uploaded files are just samples of what we like. "Marvo" means "owl" in French, we want an owl to be on the logo. Coffee related logo design is best, but we are open to other ideas. Size of this particular packaging is 14x14x12 cm

Target Market(s)

Online Retail

Industry/Entity Type

It Company

Logo Text

"Marvo Products" and "Marvo"

Font styles to use
Other font styles liked:
• Your choice

Colors

Designer to choose colors to be used in the design.

Requirements
Must have
• Owl on the logo. Product description in a word file attached.
Nice to have
• Read product description

```html
<!DOCTYPE html>
<html lang="en">
<head>
<meta charset="utf-8">
<title>Marvo Pour Over Coffee Filter Box — Dieline</title>
<link href="https://fonts.googleapis.com/css2?family=EB+Garamond:ital,wght@0,400;0,600;1,400;1,600&display=swap" rel="stylesheet">
<style>
  :root {
    --paper: #ffffff;
    --box-black: #000000;
    --copper: #c98a5a;
    --copper-light: #e6b58c;
    --copper-dark: #8a5230;
    --cream: #f3e6cf;
    --ink: #1a1a1a;
    --fold-line: #ffffff;
  }
  * { box-sizing: border-box; margin: 0; padding: 0; }
  html, body {
    width: 880px; height: 1200px; overflow: hidden;
    background: var(--paper);
    font-family: "EB Garamond", Georgia, serif;
  }
  .dieline { position: relative; width: 880px; height: 1200px; }
  .panel {
    position: absolute; background: var(--box-black); overflow: hidden;
  }
  .panel--lid      { left: 323px; top: 146px; width: 233px; height: 230px; }
  .panel--pattern  { left: 94px;  top: 376px; width: 229px; height: 230px; }
  .panel--base     { left: 323px; top: 376px; width: 233px; height: 230px; border: 1px solid var(--fold-line); }
  .panel--howto    { left: 556px; top: 376px; width: 230px; height: 230px; }
  .panel--welcome  { left: 323px; top: 606px; width: 233px; height: 229px; border-top: 1px solid var(--fold-line); }
  .panel--flap     { left: 323px; top: 835px; width: 232px; height: 230px; border-top: 1px solid var(--fold-line); }

  /* lid logo */
  .brand-lockup {
    position: absolute; left: 0; right: 0; top: 0; bottom: 0;
    display: flex; align-items: center; justify-content: center; gap: 8px;
  }
  .brand-mark {
    width: 12px; height: 12px; border-radius: 50%; background: var(--copper);
  }
  .brand-name {
    color: var(--copper); font-weight: 600; font-size: 24px; letter-spacing: 1px;
  }

  /* pattern panel */
  .cup-pattern {
    position: absolute; inset: 0;
    background: radial-gradient(circle at 40% 50%, #3a2416 0%, #120a05 55%, #000 100%);
  }

  /* instructions side, rotated */
  .howto-content {
    position: absolute; left: 0; top: 0; width: 230px; height: 230px;
    transform: rotate(90deg); transform-origin: 50% 50%;
    padding: 16px 26px 12px 24px; color: var(--paper);
  }
  .howto-brand {
    display: flex; align-items: center; justify-content: center; gap: 6px; margin-top: 4px;
  }
  .howto-brand .brand-mark { width: 9px; height: 9px; }
  .howto-brand .brand-name { font-size: 17px; }
  .section-title {
    display: flex; align-items: center; gap: 8px; margin: 14px 0 10px;
    font-size: 7px; letter-spacing: 1px; text-transform: uppercase;
  }
  .section-title::before, .section-title::after {
    content: ""; flex: 1; height: 1px; background: currentColor; opacity: 0.8;
  }
  .howto-steps { list-style: none; font-size: 5.2px; line-height: 1.45; text-align: justify; }

  /* welcome card, printed upside down */
  .welcome-card {
    position: absolute; left: 15px; top: 17px; width: 203px; height: 196px;
    padding: 5px;
    background: linear-gradient(135deg, var(--copper-dark), var(--copper-light) 40%, var(--copper) 60%, var(--cream));
    transform: rotate(180deg);
  }
  .welcome-card__inner {
    width: 100%; height: 100%; background: var(--paper); color: var(--ink);
    padding: 14px 12px 10px; font-size: 4.1px; line-height: 1.45;
  }
  .welcome-card__greeting {
    text-align: center; font-style: italic; font-weight: 600; font-size: 5.5px; margin-bottom: 4px;
  }
  .welcome-card__intro { text-align: center; font-style: italic; margin-bottom: 4px; }
  .welcome-card .section-title { margin: 8px 0 6px; font-size: 4.5px; color: var(--ink); }
  .welcome-card__tip { margin-bottom: 2px; text-align: justify; }
</style>
</head>
<body>
<main class="dieline">

  <section class="panel panel--lid">
    <div class="brand-lockup">
      <span class="brand-mark"></span>
      <span class="brand-name">MARVO</span>
    </div>
  </section>

  <section class="panel panel--pattern">
    <div class="cup-pattern" role="img" aria-label="Repeating pattern of copper coffee cups with rising steam lines on black"></div>
  </section>

  <section class="panel panel--base"></section>

  <section class="panel panel--howto">
    <div class="howto-content">
      <div class="howto-brand">
        <span class="brand-mark"></span>
        <span class="brand-name">MARVO</span>
      </div>
      <h2 class="section-title">Instructions</h2>
      <ol class="howto-steps">
        <li>1. Place filter on your favorite mug and fill with a desired amount of coffee, we recommend 2-3 tablespoons per cup of coffee.</li>
        <li>2. Pre-infuse your coffee by pouring just enough hot water to allow water to soak through the grounds for 30 seconds.</li>
        <li>3. Pour the desired amount of water onto your pre-infused coffee in a circular motion. Be careful not to pour too much at once.</li>
        <li>4. It should take about three minutes for a 6-ounce cup of coffee to finish dripping.</li>
        <li>5. Sit back and enjoy your cup of coffee!</li>
      </ol>
    </div>
  </section>

  <section class="panel panel--welcome">
    <div class="welcome-card">
      <div class="welcome-card__inner">
        <p class="welcome-card__greeting">Hello there!</p>
        <p class="welcome-card__intro">Thank you for purchasing one of the Marvo products! We hope you enjoy every cup, we like our coffee fresh and hot and so we strive to share our experience with you! We have put together a few tips on how to make your coffee experience the best, so check it out!</p>
        <p class="welcome-card__intro">Word of wisdom from the Marvo team: a good cup of coffee shared with a friend is like capturing happiness in a cup! Share the liquid gold with others!</p>
        <h2 class="section-title">Tips and Tricks</h2>
        <p class="welcome-card__tip">To make the best cup of coffee, make sure your grind is not too coarse and not too fine, it has to be just right! We generally recommend a medium-coarse grind to achieve the best results.</p>
        <p class="welcome-card__tip">The darker the roast of your coffee the more spicy and bittersweet it will taste. Light roasts retain more of the caffeine from the coffee bean.</p>
        <p class="welcome-card__tip">The optimum temperature for pour over coffee water is 195 to 205 degrees Fahrenheit. You can achieve this by bringing your water to a boil and then letting it sit for about 30 seconds to a minute.</p>
        <p class="welcome-card__tip">Pre-infusion: this is a very important step when using a pour over coffee filter. Pour just enough water onto the coffee to allow water to soak through the grounds. Give it a minute or so before brewing your coffee.</p>
        <p class="welcome-card__tip">We recommend keeping the spout of the kettle as close to the brew bed as possible, pouring onto — not through — the coffee bed. After pre-infusion, pour softly in a circular pattern.</p>
      </div>
    </div>
  </section>

  <section class="panel panel--flap"></section>

</main>
</body>
</html>
```